***Design a Nutritional Supplement Label for Bright Harvest!***

I have an existing label, I want to keep the logo but change the rest of the design. I am open to different creative ideas, but it needs to look appropriate for the shelves at Bright Harvest. This means it needs to look professional and premium, without being sterile and boring. I feel like my current label looks a little 1990s. You can play with the colors, font and design elements, while keeping the logo, descriptive text and the same layout. Feel free to take some bold chances. (You cannot change the font in the supplement facts section)

Font styles to use
Sans Serif

Colors

Designer to choose colors to be used in the design.

Requirements
Must have
• Keep the same text and layout. Keep the "Muscle Haven" logo as-is. DO NOT CHANGE THE LOGO!!

```html
<!DOCTYPE html>
<html lang="en">
<head>
<meta charset="utf-8">
<title>Muscle Haven – Supplement Label</title>
<link rel="stylesheet" href="https://fonts.googleapis.com/css2?family=Montserrat:wght@600;700&family=Lato:wght@400;700;900&family=Arimo:wght@400;700&display=swap">
<style>
  :root {
    --stage: #767676;
    --sky-light: #e4f6fc;
    --sky-mid: #8fd6f2;
    --ocean: #1c8fe0;
    --deep-blue: #1d4fd8;
    --brand-blue: #3a8fd8;
    --ink: #0f1e3a;
    --link-blue: #1f6fd1;
    --ribbon: #3f86d6;
    --ribbon-dark: #1f4f9a;
    --ribbon-fold: #163c78;
    --white: #ffffff;
  }
  * { box-sizing: border-box; margin: 0; padding: 0; }
  html, body { width: 1200px; height: 900px; overflow: hidden; }
  body {
    background: var(--stage);
    font-family: "Lato", sans-serif;
    position: relative;
  }
  .label {
    position: absolute;
    left: 60px; top: 190px;
    width: 1080px; height: 520px;
    background: linear-gradient(180deg, var(--sky-light) 0%, #c6ecf9 35%, var(--sky-mid) 62%, var(--ocean) 85%, var(--deep-blue) 100%);
    overflow: hidden;
    display: grid;
    grid-template-columns: 300px 480px 300px;
  }
  .label-waves { position: absolute; inset: 0; width: 100%; height: 100%; }
  .panel { position: relative; padding: 40px 28px; }

  /* left panel */
  .story {
    font-size: 11.5px; line-height: 1.45; color: var(--ink);
    text-align: justify; font-weight: 700; margin-top: 50px;
  }
  .story .ingredient { color: var(--link-blue); }
  .disclaimer {
    margin-top: 26px; font-size: 10px; font-weight: 900; color: var(--ink); line-height: 1.35;
  }
  .directions {
    margin-top: 26px; width: 170px; margin-left: auto;
    background: rgba(255,255,255,0.55); padding: 6px 8px;
    font-size: 8px; line-height: 1.3; color: var(--ink);
  }

  /* center panel */
  .front { text-align: center; padding-top: 48px; }
  .brand-name {
    font-family: "Montserrat", sans-serif; font-weight: 700;
    color: var(--brand-blue); line-height: 1;
  }
  .brand-name .word-main { display: block; font-size: 64px; letter-spacing: 2px; }
  .brand-name .word-sub { display: block; font-size: 30px; letter-spacing: 19px; margin-top: 10px; padding-left: 19px; }
  .claims { display: block; margin: 52px auto 0; }
  .ribbon-text { font-family: "Lato", sans-serif; font-weight: 900; font-size: 27px; fill: var(--white); letter-spacing: -0.5px; }
  .count {
    margin-top: 18px; font-family: "Montserrat", sans-serif; font-weight: 700;
    color: var(--white); font-size: 14px; letter-spacing: 2.5px; line-height: 1.75;
  }

  /* right panel */
  .facts-panel { padding-top: 80px; }
  .facts {
    font-family: "Arimo", sans-serif; color: #000;
    background: var(--white); border: 2px solid #000; padding: 5px 7px; width: 240px;
    font-size: 10px;
  }
  .facts h2 { font-size: 22px; font-weight: 700; line-height: 1; border-bottom: 1px solid #000; padding-bottom: 3px; }
  .facts .row { display: flex; justify-content: space-between; gap: 8px; padding: 2px 0; }
  .facts .amount { white-space: nowrap; }
  .facts .thick { border-bottom: 6px solid #000; }
  .facts .thin { border-bottom: 1px solid #000; }
  .facts .bold { font-weight: 700; }
  .facts .note { font-size: 8.5px; padding-top: 3px; }
  .fine-print { font-size: 9px; color: var(--ink); margin-top: 14px; line-height: 1.4; font-weight: 700; }
  .trademark { position: absolute; bottom: 38px; left: 28px; right: 28px; font-size: 8.5px; color: var(--ink); font-weight: 700; }
</style>
</head>
<body>
  <section class="label">
    <svg class="label-waves" viewBox="0 0 1080 520" preserveAspectRatio="none" aria-hidden="true">
      <path d="M0 330 C250 250 520 420 1080 300 L1080 520 L0 520 Z" fill="#5cc4ef" opacity="0.45"/>
      <path d="M0 400 C300 330 600 470 1080 370 L1080 520 L0 520 Z" fill="#2a9be6" opacity="0.5"/>
      <path d="M0 460 C320 400 640 520 1080 440 L1080 520 L0 520 Z" fill="#1d5fdc" opacity="0.6"/>
    </svg>

    <div class="panel story-panel">
      <p class="story">Magnesium is found everywhere, yet many of us face a deficiency. Stress, poor diet, low intake, and rapid excretion all add up. Muscle Haven is designed to help support healthy muscles and nerves (when used as directed) with <span class="ingredient">Puremin®</span>, a gentle form of magnesium from leafy vegetables, that is easy to assimilate.</p>
      <p class="disclaimer">*These statements have not been evaluated by the FDA. This product is not intended to diagnose, treat, cure or prevent any disease.</p>
      <p class="directions">Directions: Adults take 2 capsules daily with water. Up to 4 capsules may be taken, as most people find fast absorption. Allow 2–3 weeks for levels to be restored.</p>
    </div>

    <div class="panel front">
      <h1 class="brand-name"><span class="word-main">MUSCLE</span><span class="word-sub">HAVEN</span></h1>
      <svg class="claims" width="360" height="170" viewBox="0 0 360 170" aria-label="High Absorption, Fast Acting">
        <!-- top banner with left tail tucked behind -->
        <polygon points="64,38 2,50 22,66 4,86 66,80" fill="var(--ribbon-dark)"/>
        <polygon points="48,64 66,80 52,78" fill="var(--ribbon-fold)"/>
        <polygon points="50,24 282,12 286,62 54,76" fill="var(--ribbon)" stroke="var(--white)" stroke-width="2"/>
        <text class="ribbon-text" x="168" y="56" text-anchor="middle" transform="rotate(-3 168 50)">High Absorption</text>
        <!-- bottom banner with right tail tucked behind -->
        <polygon points="306,110 358,118 340,136 356,158 304,150" fill="var(--ribbon-dark)"/>
        <polygon points="318,140 304,150 320,152" fill="var(--ribbon-fold)"/>
        <polygon points="96,90 322,102 318,150 92,136" fill="var(--ribbon)" stroke="var(--white)" stroke-width="2"/>
        <text class="ribbon-text" x="207" y="128" text-anchor="middle" transform="rotate(3 207 120)">Fast Acting</text>
      </svg>
      <p class="count">180 CAPSULES<br>DIETARY SUPPLEMENT</p>
    </div>

    <div class="panel facts-panel">
      <div class="facts">
        <h2>Supplement Facts</h2>
        <div class="row">Serving Size 2 Capsules</div>
        <div class="row thick">Servings Per Container 90</div>
        <div class="row thin bold"><span>Amount Per Serving</span><span>% Daily Value</span></div>
        <div class="row thick"><span>Magnesium (as Puremin® magnesium glycinate)</span><span class="amount">200 mg 48%</span></div>
        <div class="note">*Daily Value based on a 2,000 calorie diet.</div>
      </div>
      <p class="fine-print">Other ingredients: vegetable cellulose capsule, rice flour.<br>Gluten free. No dairy, soy or artificial colors.</p>
      <p class="trademark">Puremin® is a registered trademark of Vita Minerals Co.</p>
    </div>
  </section>
</body>
</html>
```